Stationary for Travel & Tourism Co.
KBR Stationary
Stationary for Travel & Tourism Co. - Travel
Creative Brief
Professional
Tariq Hamdoun Salwi
IT Manager
Office No.627, Noor Plaza Al Hamra Dist. - Prince Fahd Street P.B No.38271 Jeddah 27390 Kingdom of Saudi Arabia
+966 2 6583917 X 482
marwanek@gokbrtrips.com
www.gokbrtrips.com
The horse object in the logo is advised to be nicely embosed as watermark on the stationary particularly on the letter head.

```html
<!DOCTYPE html>
<html lang="en">
<head>
<meta charset="utf-8">
<title>KBR Business Card</title>
<link href="https://fonts.googleapis.com/css2?family=Michroma&family=Open+Sans:wght@400;600&display=swap" rel="stylesheet">
<style>
  :root {
    --page-bg: #e9e6e2;
    --card-white: #fbfbfb;
    --brand-red: #b3151d;
    --brand-red-dark: #7d0c12;
    --brand-red-light: #d42a30;
    --silver-light: #f4f4f4;
    --silver-mid: #c9c9c9;
    --silver-dark: #8e8e8e;
    --ink-dark: #2b2b2b;
    --text-white: #ffffff;
    --text-soft: #f3d6d6;
  }
  * { box-sizing: border-box; margin: 0; padding: 0; }
  html, body {
    width: 1200px; height: 768px; overflow: hidden;
    background: var(--page-bg);
  }
  .business-card {
    position: absolute; left: 160px; top: 64px;
    width: 880px; height: 640px;
    background: var(--card-white);
    box-shadow: 0 14px 40px rgba(0,0,0,0.18);
    overflow: hidden;
  }
  .brand-block {
    position: absolute; left: 0; right: 0; top: 90px;
    text-align: center;
  }
  .brand-name {
    font-family: "Michroma", sans-serif;
    font-size: 92px; letter-spacing: 10px;
    color: var(--ink-dark); line-height: 1;
    display: inline-flex; align-items: center; gap: 26px;
  }
  .brand-dot {
    width: 44px; height: 44px; border-radius: 50%;
    background: var(--brand-red); display: inline-block;
  }
  .brand-tagline {
    margin-top: 18px;
    font-family: "Michroma", sans-serif;
    font-size: 19px; letter-spacing: 2px;
    color: var(--brand-red);
  }
  .silver-frame {
    position: absolute; left: 0; right: 0; top: 312px; height: 300px;
    background: linear-gradient(180deg, var(--silver-light) 0%, var(--silver-mid) 40%, var(--silver-dark) 55%, var(--silver-mid) 75%, var(--silver-light) 100%);
  }
  .red-band {
    position: absolute; left: 0; right: 0; top: 326px; height: 268px;
    background: linear-gradient(180deg, var(--brand-red-light) 0%, var(--brand-red) 45%, var(--brand-red-dark) 100%);
  }
  .band-notch {
    position: absolute; left: 208px; top: 326px;
    width: 0; height: 0;
    border-left: 18px solid transparent;
    border-right: 18px solid transparent;
    border-top: 18px solid var(--ink-dark);
  }
  .band-divider {
    position: absolute; left: 556px; top: 346px; width: 2px; height: 228px;
    background: linear-gradient(180deg, rgba(255,255,255,0), rgba(255,255,255,0.5), rgba(255,255,255,0));
  }
  .holder {
    position: absolute; left: 52px; top: 362px;
    color: var(--text-white);
  }
  .holder-name {
    font-family: "Michroma", sans-serif;
    font-size: 22px; letter-spacing: 1px;
  }
  .holder-title {
    margin-top: 10px;
    font-family: "Open Sans", sans-serif;
    font-size: 17px; color: var(--text-soft);
  }
  .contact-list {
    position: absolute; left: 580px; top: 350px; width: 290px;
    list-style: none;
    font-family: "Open Sans", sans-serif;
    font-size: 12.5px; line-height: 1.45;
    color: var(--text-white);
  }
  .contact-item {
    display: flex; align-items: flex-start; gap: 10px;
    margin-bottom: 7px;
  }
  .contact-icon {
    flex: 0 0 18px; width: 18px; height: 18px; margin-top: 1px;
  }
</style>
</head>
<body>
  <div class="business-card">
    <div class="brand-block">
      <div class="brand-name"><span class="brand-dot"></span>KBR</div>
      <div class="brand-tagline">KEEN BORDERS TRAVEL &amp; TOURISM CO</div>
    </div>

    <div class="silver-frame"></div>
    <div class="red-band"></div>
    <div class="band-notch"></div>
    <div class="band-divider"></div>

    <div class="holder">
      <div class="holder-name">Tariq Hamdoun Salwi</div>
      <div class="holder-title">IT Manager</div>
    </div>

    <ul class="contact-list">
      <li class="contact-item">
        <svg class="contact-icon" viewBox="0 0 18 18"><circle cx="9" cy="9" r="9" fill="#fff"/><path d="M9 4a3 3 0 0 1 3 3c0 2.3-3 6-3 6s-3-3.7-3-6a3 3 0 0 1 3-3z" fill="#b3151d"/><circle cx="9" cy="7" r="1" fill="#fff"/></svg>
        <span>Office No.627, Noor Plaza<br>Al Hamra Dist. - Prince Fahd Street<br>P.B No.38271 Jeddah 27390<br>Kingdom of Saudi Arabia</span>
      </li>
      <li class="contact-item">
        <svg class="contact-icon" viewBox="0 0 18 18"><circle cx="9" cy="9" r="9" fill="#fff"/><path d="M5.5 4.5l2 0 1 2.5-1.2 1a6 6 0 0 0 2.7 2.7l1-1.2 2.5 1v2a1 1 0 0 1-1 1A8 8 0 0 1 4.5 5.5a1 1 0 0 1 1-1z" fill="#b3151d"/></svg>
        <span>+966 2 6583917 X 482</span>
      </li>
      <li class="contact-item">
        <svg class="contact-icon" viewBox="0 0 18 18"><circle cx="9" cy="9" r="9" fill="#fff"/><rect x="6" y="3.5" width="6" height="11" rx="1" fill="#b3151d"/><rect x="7" y="5" width="4" height="6.5" fill="#fff"/></svg>
        <span>+966 507284316</span>
      </li>
      <li class="contact-item">
        <svg class="contact-icon" viewBox="0 0 18 18"><circle cx="9" cy="9" r="9" fill="#fff"/><rect x="4" y="7" width="10" height="6" rx="1" fill="#b3151d"/><rect x="6" y="4" width="6" height="4" fill="#b3151d"/><rect x="6" y="10" width="6" height="1" fill="#fff"/></svg>
        <span>+966 2 6749052</span>
      </li>
      <li class="contact-item">
        <svg class="contact-icon" viewBox="0 0 18 18"><circle cx="9" cy="9" r="9" fill="#fff"/><rect x="4" y="5.5" width="10" height="7" fill="#b3151d"/><path d="M4 5.5l5 4 5-4" fill="none" stroke="#fff" stroke-width="1"/></svg>
        <span>marwanek@gokbrtrips.com</span>
      </li>
      <li class="contact-item">
        <svg class="contact-icon" viewBox="0 0 18 18"><circle cx="9" cy="9" r="9" fill="#fff"/><circle cx="9" cy="9" r="5" fill="none" stroke="#b3151d" stroke-width="1.2"/><ellipse cx="9" cy="9" rx="2.2" ry="5" fill="none" stroke="#b3151d" stroke-width="1"/><path d="M4 9h10" stroke="#b3151d" stroke-width="1"/></svg>
        <span>www.gokbrtrips.com</span>
      </li>
    </ul>
  </div>
</body>
</html>
```